Meadow Lantern Veterinary Practice including Nest2Grow

We require a double-sided full colour tri-fold Brochure for Print.
Colour theme to in line with logo below

Written CONTENT below
Orphans
We can provide care and a new mother for orphan foals of any age, breed or size, from thoroughbreds and draft breeds to tiny ponies and even donkeys.
We have successfully fostered orphans from a few hours of age through to eight weeks, regardless of how long or if at all they were with their birth mother, and of previous fostering attempts.
We have the knowledge and experience to provide optimum nutrition and care to orphans during the brief period that they don’t have a mum, until their new foster mother is ready to take them.
Additionally we are a veterinary practice, and can provide diagnostics and therapeutics for compromised orphan foals such as plasma administration and health checks.

Mares
Nest2Grow mares have been selected for mothering ability and temperament, and have all carried and raised at least one foal of their own. Many have already been successful foster mothers in one or more of the last five breeding seasons.
The mares are not currently pregnant and are given a carefully designed course of hormones to induce lactation when required. The milk produced is not colostrum, but is completely normal and equivalent to that which they would have had if the foal was theirs by birth.
There is published scientific information (in addition to our own experience and that of the owners of previous graduates of our programme) that growth and development of foals raised by induced lactation is identical to that of foals raised by their birth mothers.

Fostering
During the few days when the mare’s udder is developing, mare and foal are kept next separately but in close proximity, allowing bonding to begin and reducing stress on the orphan.
The fostering is completed once the mare has enough milk to feed the foal, and our experienced handlers ensure that joining the two goes smoothly.
Once they are together the mare completely accepts the foal as her own, and the foal can suckle freely – at this stage we continue to offer supplementary feeds until they are not needed.
The mare and foal are then a normal unit and can return to the foal owner’s care until weaning – ensuring optimum nutrition and behaviour for the foal and excellent outcomes in performance, relationships with other horses, and interaction with humans.

Complete Safety
Mares recognise their birth foal by scent - a unique bond established during the first few minutes of the foal’s life - and only a small percentage of mares who have lost their own foal will readily accept a substitute.
When a mare who has lost her birth foal is offered an orphan, it is very normal and common for her to respond with aggression - to the danger of the foal and the human handler.
Nest2Grow mares have no birth foal in the current season, and are happy to adopt any foal who is placed close to them during the hormone treatment period.
This makes for total foal and handler safety.

Excellent Success Rate
After seven years of perfecting the fostering method, Nest2Grow can claim total success: we have now documented almost 50 fosterings over the last five breeding seasons. We have never been entrusted with an orphan foal that we have not been able to provide with a beautiful foster mum.

Career Mothers
Being dedicated career mothers with no other job in life, our mares are free to accompany their new foals home and stay with them as long as required. No foals are weaned and left without a mother in our programme, and our beautiful mares who would otherwise not be bred, are given a foal every year and a wonderful lifelong purpose.

Every single orphan’s human family has admired and appreciated our beautiful mares, with many offering to give them a home for life. Each season as the orphans are weaned, we welcome our mares home to Meadow Lantern to prepare for the next foal in need – a job they totally love! – just as if they were in a natural breeding situation.

Meadow Lantern Vet Practice including Nest2Grow
214 Pellerby Lane
Thornvale. Vic. 3812

Phone 0431958617 or 0419284056

```html
<!DOCTYPE html>
<html lang="en">
<head>
<meta charset="utf-8">
<title>Meadow Lantern Veterinary Practice – Tri-fold Brochure</title>
<link href="https://fonts.googleapis.com/css2?family=Open+Sans:ital,wght@0,400;0,600;0,700;1,400&family=Oswald:wght@500;600&display=swap" rel="stylesheet">
<style>
  :root {
    --orange: #e8822a;
    --orange-deep: #d96f1c;
    --wood-dark: #3b2213;
    --wood-mid: #6a3d20;
    --wood-light: #8a5530;
    --paper: #ffffff;
    --ink: #4a4440;
    --tan: #c9b9a0;
    --bg: #e6e6e6;
    --photo-green: #6f7d52;
    --photo-brown: #7a4a2a;
  }
  * { box-sizing: border-box; margin: 0; padding: 0; }
  html, body { width: 1200px; height: 2400px; overflow: hidden; }
  body { background: var(--bg); font-family: "Open Sans", Arial, sans-serif; color: var(--ink); }

  .spread {
    position: absolute; left: 50px; width: 1100px; height: 780px;
    display: flex; box-shadow: 0 10px 30px rgba(0,0,0,0.18);
  }
  .spread--outside { top: 280px; }
  .spread--inside { top: 1340px; }

  .panel { position: relative; width: 366.67px; height: 100%; overflow: hidden; }
  .panel--white { background: var(--paper); }
  .panel--wood {
    background: linear-gradient(90deg, var(--wood-dark) 0%, var(--wood-mid) 35%, var(--wood-light) 55%, var(--wood-mid) 75%, var(--wood-dark) 100%);
    color: #f3e9de;
  }

  .photo { position: absolute; }
  .photo--field { background: linear-gradient(160deg, #9aa487 0%, var(--photo-green) 45%, var(--photo-brown) 100%); }
  .photo--portrait { background: linear-gradient(160deg, #5b4f45 0%, #7d6a55 50%, #4a3a2c 100%); }
  .photo--foal { background: linear-gradient(160deg, #4f5d2c 0%, #8a5a2c 55%, #6b7a35 100%); }
  .photo--dark { background: linear-gradient(160deg, #1f1a16 0%, #4a3020 60%, #2a211b 100%); }

  .curve { position: absolute; left: 0; width: 100%; }

  .brand { display: flex; align-items: center; gap: 10px; }
  .brand__dot { width: 26px; height: 26px; border-radius: 50%; background: var(--orange); flex: none; }
  .brand__name { font-family: "Open Sans", Arial, sans-serif; font-weight: 600; color: var(--orange); font-size: 30px; letter-spacing: -0.3px; }

  .heading {
    font-family: "Oswald", "Arial Narrow", sans-serif; font-weight: 600;
    color: var(--orange); font-size: 17px; letter-spacing: 0.5px; text-transform: uppercase;
    margin-bottom: 6px;
  }
  .copy p { font-size: 10.2px; line-height: 1.45; margin-bottom: 6px; }
  .copy--dark p { color: var(--ink); }
  .copy--light p { color: #f3e9de; }

  /* Outside panel 1 */
  .badge {
    position: absolute; left: 36px; top: 190px; width: 118px; height: 118px; border-radius: 50%;
    background: var(--orange); border: 4px solid var(--paper);
    display: flex; align-items: center; justify-content: center; text-align: center;
    font-family: "Oswald", sans-serif; font-weight: 500; color: var(--paper); font-size: 13px; line-height: 1.2;
    text-transform: uppercase; padding: 12px;
  }
  .career { position: absolute; left: 28px; right: 28px; top: 350px; }

  /* Back panel */
  .contact { position: absolute; left: 0; right: 0; top: 40px; text-align: center; padding: 0 30px; }
  .contact__circle {
    width: 130px; height: 130px; border-radius: 50%; margin: 0 auto 30px;
    border: 4px solid var(--tan);
  }
  .contact .brand { justify-content: center; margin-bottom: 22px; }
  .contact .brand__name { font-size: 26px; }
  .contact__line { font-size: 11px; line-height: 1.6; color: #f3e9de; }
  .contact__call {
    font-family: "Oswald", sans-serif; font-weight: 500; color: var(--orange);
    font-size: 19px; letter-spacing: 0.5px; margin: 22px 0 10px;
  }
  .phone-pill {
    display: inline-flex; align-items: center; gap: 10px;
    background: var(--orange); color: var(--paper); border-radius: 16px;
    padding: 5px 22px; font-weight: 700; font-size: 16px;
  }
  .contact__email { font-size: 11px; margin-top: 10px; color: #f3e9de; }
  .social { display: flex; justify-content: center; gap: 16px; margin-top: 28px; }
  .social__dot { width: 22px; height: 22px; border-radius: 50%; background: var(--orange); }
  .website {
    position: absolute; left: 0; right: 0; bottom: 38px; text-align: center;
    font-family: "Oswald", sans-serif; font-weight: 500; color: var(--orange); font-size: 17px; letter-spacing: 0.5px;
  }

  /* Front panel */
  .front-brand { position: absolute; left: 30px; top: 42px; }
  .front-brand .brand__name { font-size: 31px; }
  .front-tagline {
    position: absolute; left: 68px; top: 86px; font-size: 8px; letter-spacing: 3px;
    color: var(--orange); text-transform: uppercase;
  }
  .front-title {
    position: absolute; left: 20px; right: 20px; bottom: 34px; text-align: center;
    color: var(--paper); font-size: 19px; line-height: 1.35; font-weight: 400;
  }

  /* Inside panel 1 */
  .orphans { position: absolute; left: 26px; right: 26px; top: 412px; }
  .inset-circle {
    position: absolute; left: 120px; top: 272px; width: 96px; height: 96px; border-radius: 50%;
    border: 4px solid var(--paper);
  }

  /* Inside panel 2 */
  .mares { position: absolute; left: 28px; right: 28px; top: 34px; }
  .mares .heading + .heading, .mares .fostering-head { margin-top: 10px; }

  /* Inside panel 3 */
  .safety { position: absolute; left: 26px; right: 26px; top: 30px; }
</style>
</head>
<body>

<!-- Outside of the brochure -->
<section class="spread spread--outside" aria-label="Brochure outside">

  <!-- Inner flap: Career Mothers -->
  <article class="panel panel--white">
    <div class="photo photo--portrait" style="left:0;top:0;width:100%;height:280px;" role="img" aria-label="Photo of a woman standing with a mare and foal"></div>
    <svg class="curve" style="top:230px;height:100px;" viewBox="0 0 367 100" preserveAspectRatio="none" aria-hidden="true">
      <path d="M0 40 Q183 95 367 15 L367 100 L0 100 Z" fill="#ffffff"/>
      <path d="M0 40 Q183 95 367 15" fill="none" stroke="#c9b9a0" stroke-width="4"/>
    </svg>
    <div class="badge">Veterinary practice including Nest2Grow</div>
    <div class="career copy copy--dark">
      <h2 class="heading">Career Mothers</h2>
      <p>Being dedicated career mothers with no other job in life, our mares are free to accompany their new foals home and stay with them as long as required. No foals are weaned and left without a mother in our programme, and our beautiful mares who would otherwise not be bred, are given a foal every year and a wonderful lifelong purpose.</p>
      <p>Every single orphan’s human family has admired and appreciated our beautiful mares, with many offering to give them a home for life.</p>
      <p>Each season as the orphans are weaned, we welcome our mares home to Meadow Lantern to prepare for the next foal in need – a job they totally love! – just as if they were in a natural breeding situation.</p>
    </div>
  </article>

  <!-- Back panel: contact -->
  <article class="panel panel--wood">
    <div class="contact">
      <div class="contact__circle photo photo--field" style="position:relative;" role="img" aria-label="Round photo of mares grazing in a paddock"></div>
      <div class="brand"><span class="brand__dot"></span><span class="brand__name">Meadow Lantern</span></div>
      <p class="contact__line">Meadow Lantern Veterinary Practice<br>is located at</p>
      <p class="contact__line">214 Pellerby Lane<br>Thornvale. Vic. 3812</p>
      <p class="contact__call">PLEASE CALL FOR AN APPOINTMENT</p>
      <span class="phone-pill">
        <svg width="16" height="16" viewBox="0 0 24 24" aria-hidden="true"><path fill="#fff" d="M6.6 10.8a15.1 15.1 0 0 0 6.6 6.6l2.2-2.2a1 1 0 0 1 1-.25 11.4 11.4 0 0 0 3.6.57 1 1 0 0 1 1 1V20a1 1 0 0 1-1 1A17 17 0 0 1 3 4a1 1 0 0 1 1-1h3.5a1 1 0 0 1 1 1c0 1.25.2 2.45.57 3.57a1 1 0 0 1-.25 1z"/></svg>
        0419 284 056
      </span>
      <p class="contact__email">admin@meadowlanternvet.com.au</p>
      <div class="social"><span class="social__dot"></span><span class="social__dot"></span></div>
    </div>
    <p class="website">www.meadowlanternvet.com.au</p>
  </article>

  <!-- Front cover -->
  <article class="panel panel--white">
    <div class="photo photo--field" style="left:0;top:150px;width:100%;height:520px;" role="img" aria-label="Photo of a chestnut mare walking with her foal in a paddock"></div>
    <svg class="curve" style="top:110px;height:80px;" viewBox="0 0 367 80" preserveAspectRatio="none" aria-hidden="true">
      <path d="M0 0 L367 0 L367 30 Q183 80 0 45 Z" fill="#ffffff"/>
      <path d="M367 30 Q183 80 0 45" fill="none" stroke="#c9b9a0" stroke-width="4"/>
    </svg>
    <div class="front-brand brand"><span class="brand__dot"></span><span class="brand__name">Meadow Lantern</span></div>
    <p class="front-tagline">Veterinary Practice</p>
    <svg class="curve" style="bottom:0;height:170px;" viewBox="0 0 367 170" preserveAspectRatio="none" aria-hidden="true">
      <path d="M0 40 Q183 0 367 10 L367 170 L0 170 Z" fill="#e8822a"/>
      <path d="M0 40 Q183 0 367 10" fill="none" stroke="#ffffff" stroke-width="3"/>
    </svg>
    <h1 class="front-title">Meadow Lantern Veterinary Practice<br>including Nest2Grow</h1>
  </article>
</section>

<!-- Inside of the brochure -->
<section class="spread spread--inside" aria-label="Brochure inside">

  <!-- Orphans -->
  <article class="panel panel--wood">
    <div class="photo photo--foal" style="left:0;top:0;width:100%;height:330px;" role="img" aria-label="Photo of a young foal lying in the grass"></div>
    <svg class="curve" style="top:300px;height:80px;" viewBox="0 0 367 80" preserveAspectRatio="none" aria-hidden="true">
      <path d="M0 30 Q183 0 367 25 L367 55 Q183 30 0 60 Z" fill="#e8822a"/>
    </svg>
    <div class="inset-circle photo photo--portrait" role="img" aria-label="Round photo of a handler feeding an orphan foal"></div>
    <div class="orphans copy copy--light">
      <h2 class="heading">Orphans</h2>
      <p>We can provide care and a new mother for orphan foals of any age, breed or size, from thoroughbreds and draft breeds to tiny ponies and even donkeys.</p>
      <p>We have successfully fostered orphans from a few hours of age through to eight weeks, regardless of how long or if at all they were with their birth mother, and of previous fostering attempts.</p>
      <p>We have the knowledge and experience to provide optimum nutrition and care to orphans during the brief period that they don’t have a mum, until their new foster mother is ready to take them.</p>
      <p>Additionally we are a veterinary practice, and can provide diagnostics and therapeutics for compromised orphan foals such as plasma administration and health checks.</p>
    </div>
  </article>

  <!-- Mares & Fostering -->
  <article class="panel panel--white">
    <div class="mares copy copy--dark">
      <h2 class="heading">Mares</h2>
      <p>Nest2Grow mares have been selected for mothering ability and temperament, and have all carried and raised at least one foal of their own. Many have already been successful foster mothers in one or more of the last five breeding seasons.</p>
      <p>The mares are not currently pregnant and are given a carefully designed course of hormones to induce lactation when required. The milk produced is not colostrum, but is completely normal and equivalent to that which they would have had if the foal was theirs by birth.</p>
      <p>There is published scientific information (in addition to our own experience and that of the owners of previous graduates of our programme) that growth and development of foals raised by induced lactation is identical to that of foals raised by their birth mothers.</p>
      <h2 class="heading fostering-head">Fostering</h2>
      <p>During the few days when the mare’s udder is developing, mare and foal are kept separately but in close proximity, allowing bonding to begin and reducing stress on the orphan.</p>
      <p>The fostering is completed once the mare has enough milk to feed the foal, and our experienced handlers ensure that joining the two goes smoothly.</p>
      <p>Once they are together the mare completely accepts the foal as her own, and the foal can suckle freely – at this stage we continue to offer supplementary feeds until they are not needed.</p>
      <p>The mare and foal are then a normal unit and can return to the foal owner’s care until weaning – ensuring optimum nutrition and behaviour for the foal and excellent outcomes in performance, relationships with other horses, and interaction with humans.</p>
    </div>
  </article>

  <!-- Complete Safety & Success Rate -->
  <article class="panel panel--wood">
    <div class="safety copy copy--light">
      <h2 class="heading">Complete Safety</h2>
      <p>Mares recognise their birth foal by scent - a unique bond established during the first few minutes of the foal’s life - and only a small percentage of mares who have lost their own foal will readily accept a substitute.</p>
      <p>When a mare who has lost her birth foal is offered an orphan, it is very normal and common for her to respond with aggression - to the danger of the foal and the human handler.</p>
      <p>Nest2Grow mares have no birth foal in the current season, and are happy to adopt any foal who is placed close to them during the hormone treatment period.</p>
      <p>This makes for total foal and handler safety.</p>
      <h2 class="heading" style="margin-top:10px;">Excellent Success Rate</h2>
      <p>After seven years of perfecting the fostering method, Nest2Grow can claim total success: we have now documented almost 50 fosterings over the last five breeding seasons. We have never been entrusted with an orphan foal that we have not been able to provide with a beautiful foster mum.</p>
    </div>
    <div class="photo photo--dark" style="left:0;bottom:0;width:100%;height:220px;" role="img" aria-label="Photo of a mare nuzzling her foal in a stable"></div>
    <svg class="curve" style="bottom:190px;height:60px;" viewBox="0 0 367 60" preserveAspectRatio="none" aria-hidden="true">
      <path d="M0 10 Q183 45 367 20 L367 35 Q183 60 0 30 Z" fill="#e8822a"/>
      <path d="M0 30 Q183 60 367 35 L367 60 L0 60 Z" fill="#2a211b" opacity="0"/>
    </svg>
  </article>
</section>

</body>
</html>
```